Letterhead for Law Firm Harborstone Law Group

This would be for virtual letterhead, business cards, etc.

Also logo. I am happy to pay extra for that if it is a separate project.

Harborstone Law Group

482 Alder Court, Suite 730
San Francisco, California 94387

Target Market(s)

Business law services.

Industry/Entity Type

Business

Colors

Designer to choose colors to be used in the design.

```html
<!DOCTYPE html>
<html lang="en">
<head>
<meta charset="utf-8">
<title>Harborstone Law Group — Business Card</title>
<link rel="stylesheet" href="https://fonts.googleapis.com/css2?family=Open+Sans:wght@300;400&display=swap">
<style>
  :root {
    --backdrop: #a6a6a6;
    --card-white: #ffffff;
    --card-mist: #e6e8ea;
    --brand-red: #d23a22;
    --charcoal: #2e2f30;
    --charcoal-light: #4a4b4c;
    --ink: #2b2b2b;
    --ink-soft: #444546;
    --web-text: #d8d8d8;
  }
  html, body {
    margin: 0;
    padding: 0;
    width: 959px;
    height: 1200px;
    overflow: hidden;
    background: var(--backdrop);
    font-family: "Open Sans", sans-serif;
  }
  .sheet {
    position: relative;
    width: 959px;
    height: 1200px;
  }
  .card {
    position: absolute;
    left: 38px;
    width: 884px;
    height: 553px;
    overflow: hidden;
    background: radial-gradient(ellipse at 55% 55%, var(--card-white) 30%, #f2f3f4 65%, var(--card-mist) 100%);
  }
  .card--front { top: 31px; }
  .card--back  { top: 612px; }
  .card__art {
    position: absolute;
    inset: 0;
    width: 100%;
    height: 100%;
  }
  .wordmark {
    position: absolute;
    display: flex;
    align-items: center;
    gap: 14px;
    color: var(--ink);
    font-weight: 300;
    white-space: nowrap;
  }
  .wordmark__square {
    background: var(--brand-red);
    flex: none;
  }
  .card--front .wordmark {
    left: 0;
    right: 0;
    top: 228px;
    justify-content: center;
    font-size: 44px;
    padding-right: 20px;
  }
  .card--front .wordmark__square { width: 26px; height: 26px; }
  .card--back .wordmark {
    left: 31px;
    top: 34px;
    font-size: 27px;
    gap: 10px;
  }
  .card--back .wordmark__square { width: 16px; height: 16px; }
  .website {
    position: absolute;
    margin: 0;
    font-size: 19px;
    line-height: 26px;
    font-weight: 300;
    color: var(--web-text);
    letter-spacing: 0.2px;
    white-space: nowrap;
  }
  .card--front .website { left: 431px; top: 510px; }
  .card--back .website  { left: 189px; top: 508px; }
  .contact-list {
    position: absolute;
    left: 494px;
    top: 32px;
    margin: 0;
    padding: 0;
    list-style: none;
    color: var(--ink-soft);
    font-size: 17.5px;
    font-weight: 400;
    line-height: 1.25;
  }
  .contact-list__item {
    display: flex;
    align-items: center;
    gap: 11px;
    margin-bottom: 15px;
  }
  .contact-list__item--address { margin-top: 2px; }
  .contact-list__icon {
    width: 40px;
    height: 40px;
    flex: none;
  }
  .holder {
    position: absolute;
    right: 54px;
    top: 345px;
    text-align: right;
  }
  .holder__name {
    margin: 0;
    font-size: 41px;
    font-weight: 400;
    color: var(--ink-soft);
    line-height: 1.15;
  }
  .holder__role {
    display: inline-block;
    margin-top: 4px;
    padding: 0 6px;
    background: var(--brand-red);
    color: var(--card-white);
    font-size: 27px;
    font-weight: 400;
    letter-spacing: 1px;
    line-height: 34px;
  }
</style>
</head>
<body>
<main class="sheet">

  <section class="card card--front" aria-label="Card front">
    <svg class="card__art" viewBox="0 0 958 599" preserveAspectRatio="none" aria-hidden="true">
      <defs>
        <linearGradient id="charcoalSweep" x1="0" y1="0" x2="1" y2="0">
          <stop offset="0" stop-color="var(--charcoal-light)"/>
          <stop offset="1" stop-color="var(--charcoal)"/>
        </linearGradient>
      </defs>
      <path d="M0,0 H958 C700,8 300,40 0,118 Z" fill="var(--brand-red)"/>
      <path d="M0,118 C300,40 700,8 958,0 L958,3 C700,16 300,56 0,134 Z" fill="var(--charcoal)"/>
      <g class="base-swell">
        <path d="M0,536 C260,532 520,512 618,446 Q634,420 650,440 C770,510 880,565 958,594 V599 H0 Z" fill="var(--brand-red)"/>
        <path d="M0,560 C260,556 540,534 624,464 Q636,446 650,456 C770,522 880,570 958,599 H0 Z" fill="url(#charcoalSweep)"/>
      </g>
    </svg>
    <div class="wordmark"><span class="wordmark__square"></span>Harborstone Law Group</div>
    <p class="website">www.harborstonelawgroup.com</p>
  </section>

  <section class="card card--back" aria-label="Card back">
    <svg class="card__art" viewBox="0 0 958 599" preserveAspectRatio="none" aria-hidden="true">
      <defs>
        <linearGradient id="charcoalSweepBack" x1="1" y1="0" x2="0" y2="0">
          <stop offset="0" stop-color="var(--charcoal-light)"/>
          <stop offset="1" stop-color="var(--charcoal)"/>
        </linearGradient>
      </defs>
      <g transform="translate(958,0) scale(-1,1)">
        <path d="M0,536 C260,532 520,512 618,446 Q634,420 650,440 C770,510 880,565 958,594 V599 H0 Z" fill="var(--brand-red)"/>
        <path d="M0,560 C260,556 540,534 624,464 Q636,446 650,456 C770,522 880,570 958,599 H0 Z" fill="url(#charcoalSweepBack)"/>
      </g>
    </svg>

    <div class="wordmark"><span class="wordmark__square"></span>Harborstone Law Group</div>

    <ul class="contact-list">
      <li class="contact-list__item">
        <svg class="contact-list__icon" viewBox="0 0 40 40" aria-label="Phone">
          <circle cx="20" cy="20" r="20" fill="var(--brand-red)"/>
          <path d="M11,17 Q20,9 29,17 L27,20 L24,18 L24,16 Q20,14 16,16 L16,18 L13,20 Z" fill="#fff"/>
          <rect x="13" y="19" width="14" height="9" rx="1.5" fill="#fff"/>
          <circle cx="20" cy="23.5" r="2.4" fill="var(--brand-red)"/>
        </svg>
        <span>555 014 2290 (P), +91-555 017 (Fax)</span>
      </li>
      <li class="contact-list__item">
        <svg class="contact-list__icon" viewBox="0 0 40 40" aria-label="Email">
          <circle cx="20" cy="20" r="20" fill="var(--brand-red)"/>
          <rect x="11" y="13" width="18" height="13" fill="none" stroke="#fff" stroke-width="1.8"/>
          <path d="M11,13 L20,21 L29,13 M11,26 L17.5,19 M29,26 L22.5,19" fill="none" stroke="#fff" stroke-width="1.6"/>
        </svg>
        <span>marlen@harborstonelawgroup.com</span>
      </li>
      <li class="contact-list__item contact-list__item--address">
        <svg class="contact-list__icon" viewBox="0 0 40 40" aria-label="Address">
          <circle cx="20" cy="20" r="20" fill="var(--brand-red)"/>
          <path d="M9,21 L20,11 L31,21 L28,21 L28,29 L23,29 L23,23 L17,23 L17,29 L12,29 L12,21 Z" fill="#fff"/>
        </svg>
        <span>482 Alder Court, Suite 730<br>San Francisco, California 94387</span>
      </li>
    </ul>

    <div class="holder">
      <h1 class="holder__name">MARLEN ODRISCO</h1>
      <span class="holder__role">Customer Relationship</span>
    </div>

    <p class="website">www.harborstonelawgroup.com</p>
  </section>

</main>
</body>
</html>
```